Real Estate Managemene Company Needs Business Card Design

We have a logo design and just need business cards made now for our business. Please use PDF logo # 3.

Card with Information to be attached shortly.

The card is used for a real estate management company. We will need to add four other employees and their cards.

Industry/Entity Type

Real Estate

Contact Information for Business Card

Tariq Hamdan
President
3187 Thornwick Avenue
Suite C
Larkmoor Heights, OH 44208
Phone 630.417.2286
Fax 630.417.2287
Cell 630.473.8062
vantorp@mailbreeze.net

Once design is approved we will have four other employees
Omar Hamdan
Operations Manager

Nadia Hamdan
Administrative Manager

Faz Hamdan
Principal

We would need to take out the cell # 630.473.8062 out for the remaining three cards.

Requirements
Must have
• Please use logo attached

```html
<!DOCTYPE html>
<html lang="en">
<head>
<meta charset="utf-8">
<title>Vantorp Realty Management Group – Business Card</title>
<link rel="stylesheet" href="https://fonts.googleapis.com/css2?family=Cinzel:wght@500&family=Open+Sans:wght@400&display=swap">
<style>
  :root {
    --page-bg: #dfe4ea;
    --card-dark: #0b0c0e;
    --card-mid: #2a2c31;
    --card-sheen: #3a3d43;
    --band-deep: #1d3a66;
    --band-light: #3a5e96;
    --brand-text: #d7dbe6;
    --name-text: #c9cfe8;
    --title-text: #a9b6d8;
    --divider: #9aa6c8;
    --contact-text: #b9bdca;
    --icon: #7f8799;
  }
  * { margin: 0; padding: 0; box-sizing: border-box; }
  html, body {
    width: 1200px;
    height: 900px;
    overflow: hidden;
    background: var(--page-bg);
  }
  .card {
    position: absolute;
    left: 75px;
    top: 150px;
    width: 1050px;
    height: 600px;
    overflow: hidden;
    background:
      radial-gradient(ellipse 55% 45% at 50% 0%, var(--card-sheen) 0%, rgba(58,61,67,0) 100%),
      linear-gradient(100deg, var(--card-mid) 0%, var(--card-dark) 35%, #16171a 60%, var(--card-dark) 100%);
    box-shadow: 0 14px 40px rgba(20, 30, 50, 0.25);
  }
  .brand {
    position: absolute;
    top: 196px;
    left: 0;
    width: 100%;
    text-align: center;
    font-family: "Cinzel", serif;
    font-weight: 500;
    font-size: 38px;
    letter-spacing: 1px;
    color: var(--brand-text);
  }
  .name-band {
    position: absolute;
    top: 332px;
    left: 0;
    width: 100%;
    height: 64px;
    background: linear-gradient(90deg, var(--band-deep) 0%, var(--band-light) 50%, var(--band-deep) 100%);
    display: flex;
    align-items: center;
    justify-content: center;
    gap: 22px;
    padding-left: 120px;
  }
  .person-name {
    font-family: "Cinzel", serif;
    font-weight: 500;
    font-size: 36px;
    letter-spacing: 1px;
    color: var(--name-text);
  }
  .band-divider {
    width: 2px;
    height: 40px;
    background: var(--divider);
  }
  .person-title {
    font-family: "Open Sans", sans-serif;
    font-size: 24px;
    letter-spacing: 1px;
    color: var(--title-text);
  }
  .contact-list {
    position: absolute;
    top: 424px;
    left: 84px;
    list-style: none;
    font-family: "Open Sans", sans-serif;
    font-size: 24px;
    letter-spacing: 1.5px;
    color: var(--contact-text);
  }
  .contact-list li {
    display: flex;
    align-items: center;
    height: 35px;
  }
  .contact-icon {
    width: 22px;
    height: 22px;
    margin-right: 12px;
    flex: none;
  }
  .contact-icon--none { visibility: hidden; }
  .address {
    position: absolute;
    top: 424px;
    right: 85px;
    font-style: normal;
    text-align: right;
    font-family: "Open Sans", sans-serif;
    font-size: 24px;
    line-height: 35px;
    letter-spacing: 1.5px;
    color: var(--contact-text);
  }
</style>
</head>
<body>
  <section class="card">
    <div class="brand">Vantorp Realty Management Group</div>

    <div class="name-band">
      <span class="person-name">Tariq Hamdan</span>
      <span class="band-divider"></span>
      <span class="person-title">President</span>
    </div>

    <ul class="contact-list">
      <li>
        <svg class="contact-icon" viewBox="0 0 22 22" aria-hidden="true">
          <rect x="6" y="1.5" width="10" height="19" rx="2" fill="none" stroke="var(--icon)" stroke-width="1.6"/>
          <line x1="9" y1="17.5" x2="13" y2="17.5" stroke="var(--icon)" stroke-width="1.6"/>
        </svg>
        630.417.2286
      </li>
      <li>
        <svg class="contact-icon" viewBox="0 0 22 22" aria-hidden="true">
          <path d="M2 8 Q11 1 20 8 L17 10 L15 7 Q11 5.5 7 7 L5 10 Z" fill="var(--icon)"/>
          <rect x="5" y="11" width="12" height="8" rx="1.5" fill="var(--icon)"/>
        </svg>
        630.417.2287
      </li>
      <li>
        <svg class="contact-icon" viewBox="0 0 22 22" aria-hidden="true">
          <rect x="6" y="2" width="10" height="6" fill="var(--icon)"/>
          <rect x="2" y="9" width="18" height="8" rx="1.5" fill="var(--icon)"/>
          <rect x="6" y="14" width="10" height="6" fill="var(--icon)"/>
        </svg>
        630.473.8062
      </li>
      <li>
        <svg class="contact-icon contact-icon--none" viewBox="0 0 22 22" aria-hidden="true"></svg>
        vantorp@mailbreeze.net
      </li>
    </ul>

    <address class="address">
      3187 Thornwick Avenue<br>
      Suite C Larkmoor Heights,<br>
      OH 44208
    </address>
  </section>
</body>
</html>
```